Harborline Keys Realty business card design

Looking for an upscale and clean business card design and updated logo. I sell to a very high-end south Florida real estate market.
Target Market(s)
High-end real estate in south Florida real estate market
Industry/Entity Type
Real Estate Agent
Contact Information for Business Card
Harborline Keys Realty, Inc
738 West Pinecrest Ave, Suite 410/520, Fort Lauderdale, FL 33318
Carl Whitmore - Broker/Owner
954-555-0172 Direct
carlhomes@mailvista.example
Website: StayPinecrest.example
Font styles to use
Other font styles liked:
- Copperplate Gothic, Georgia, etc.
Requirements
Must have
- My photo, company name, my name and title, all info stated in Details above
Nice to have
- Luxury home design element, waterfront

```html
<!DOCTYPE html>
<html lang="en">
<head>
<meta charset="utf-8">
<title>Harborline Keys Realty – Business Card</title>
<link rel="stylesheet" href="https://fonts.googleapis.com/css2?family=Arimo:wght@400&family=Arvo:wght@700&family=Libre+Baskerville:wght@400&display=swap">
<style>
  :root {
    --sun: #f5c736;
    --paper: #ffffff;
    --ink: #111111;
    --band: #000000;
    --stage: #2a2a2a;
    --photo-light: #e6e4df;
    --photo-mid: #9a8e86;
    --photo-suit: #2c3f86;
  }
  * { margin: 0; padding: 0; box-sizing: border-box; }
  html, body { width: 1200px; height: 1015px; overflow: hidden; }
  body {
    background: var(--stage);
    display: flex;
    flex-direction: column;
    align-items: center;
    justify-content: center;
    gap: 60px;
    font-family: "Arimo", Arial, sans-serif;
  }
  .card {
    position: relative;
    width: 700px;
    height: 400px;
    overflow: hidden;
  }

  /* Back side */
  .card--back { background: var(--sun); }
  .card--back .brand {
    position: absolute;
    left: 0; right: 0; top: 0; bottom: 0;
    display: flex;
    align-items: center;
    justify-content: center;
    gap: 22px;
  }
  .brand__dot {
    width: 74px; height: 74px;
    border-radius: 50%;
    background: var(--paper);
  }
  .card--back .brand__name {
    font-family: "Libre Baskerville", Georgia, serif;
    color: var(--paper);
    font-size: 34px;
    line-height: 1.25;
  }

  /* Front side */
  .card--front { background: var(--paper); color: var(--ink); }
  .card--front .brand {
    position: absolute;
    left: 52px; top: 54px;
    display: flex;
    align-items: center;
    gap: 14px;
  }
  .card--front .brand__dot { width: 46px; height: 46px; background: var(--sun); }
  .card--front .brand__name {
    font-family: "Libre Baskerville", Georgia, serif;
    font-size: 17px;
    color: var(--ink);
  }
  .address {
    position: absolute;
    left: 60px; top: 180px;
    font-size: 18px;
    line-height: 1.3;
  }
  .contact {
    position: absolute;
    left: 60px; top: 272px;
    list-style: none;
    font-size: 18px;
    line-height: 1.35;
  }
  .contact li { display: flex; align-items: center; gap: 10px; }
  .contact svg { width: 18px; height: 18px; fill: var(--sun); }

  .portrait-frame {
    position: absolute;
    left: 436px; top: 30px;
    width: 232px; height: 222px;
    border: 3px solid var(--sun);
    padding: 8px;
  }
  .portrait {
    width: 100%; height: 100%;
    background: linear-gradient(160deg, var(--photo-light) 0%, var(--photo-light) 40%, var(--photo-mid) 65%, var(--photo-suit) 85%);
  }
  .agent {
    position: absolute;
    right: 34px; top: 262px;
    text-align: right;
  }
  .agent__name {
    font-family: "Arvo", Georgia, serif;
    font-weight: 700;
    color: var(--sun);
    font-size: 28px;
    line-height: 1;
  }
  .agent__title { font-size: 16px; margin-top: 2px; }

  .accent-strip {
    position: absolute;
    left: 0; bottom: 0;
    width: 440px; height: 14px;
    background: var(--sun);
  }
  .web-band {
    position: absolute;
    right: 0; bottom: 0;
    width: 300px; height: 72px;
    background: var(--band);
    clip-path: polygon(0 0, 100% 0, 100% 100%, 6% 100%, 8% 70%, 0 70%);
    display: flex;
    align-items: center;
    justify-content: flex-end;
    padding-right: 28px;
    color: var(--sun);
    font-size: 17px;
  }
</style>
</head>
<body>
  <section class="card card--back">
    <div class="brand">
      <span class="brand__dot"></span>
      <span class="brand__name">Harborline Keys<br>Realty, Inc.</span>
    </div>
  </section>

  <section class="card card--front">
    <div class="brand">
      <span class="brand__dot brand__dot"></span>
      <span class="brand__name">Harborline Keys Realty, Inc.</span>
    </div>

    <address class="address" style="font-style:normal">
      738 West Pinecrest Ave<br>
      Suite 410/520, Fort Lauderdale<br>
      FL 33318
    </address>

    <ul class="contact">
      <li>
        <svg viewBox="0 0 24 24" aria-hidden="true"><path d="M6.6 10.8a15.1 15.1 0 0 0 6.6 6.6l2.2-2.2a1 1 0 0 1 1-.25 11.4 11.4 0 0 0 3.6.57 1 1 0 0 1 1 1V20a1 1 0 0 1-1 1A17 17 0 0 1 3 4a1 1 0 0 1 1-1h3.5a1 1 0 0 1 1 1c0 1.25.2 2.45.57 3.57a1 1 0 0 1-.25 1z"/></svg>
        954-555-0172 Direct
      </li>
      <li>
        <svg viewBox="0 0 24 24" aria-hidden="true"><path d="M2 5h20v14H2zm2 2v.5l8 5 8-5V7l-8 5z"/></svg>
        carlhomes@mailvista.example
      </li>
    </ul>

    <div class="portrait-frame">
      <div class="portrait" role="img" aria-label="Portrait photo of the broker in a blue blazer and pink shirt against a light wall"></div>
    </div>

    <div class="agent">
      <div class="agent__name">Carl Whitmore</div>
      <div class="agent__title">Broker/Owner</div>
    </div>

    <div class="accent-strip"></div>
    <div class="web-band">www.StayPinecrest.example</div>
  </section>
</body>
</html>
```